Marova Hand Wash

Design hand washes. Total 12 variants to be designed.

Variants name are:

1) MILK &OLIVE
2) Shea Butter
3) Hidden Glow
4) Cream and Peach
5) Milk and Honey
6) Amber Riddle
7) Bakhour
8) Musk
9) White Oud
10) Black Oud
11) Rose Oud
12) Oud & Sandalwood

Labels can be on transparent sticker or background colors. All variants will be differentiated by fragrances and color. Bottle will be transparent. Pumps used for dispensing will be in Black or Transparent Color.

Designers can initially present designs of 4-5 variants initially. Later based on feedback, they can work out on more.

Bottle is 400ml and shape is rectangle. Ignore the size on bottle picture. Bottle keyline is attached.

Target Market(s)

B+, B, C+

Requirements
Must have
• Some relation to the variant names

```html
<!DOCTYPE html>
<html lang="en">
<head>
<meta charset="utf-8">
<title>Marova Hand Wash Labels</title>
<link rel="stylesheet" href="https://fonts.googleapis.com/css2?family=Berkshire+Swash&family=Great+Vibes&family=Playfair+Display:wght@600&family=Tinos:wght@700&display=swap">
<style>
  :root {
    --canvas: #ffffff;
    --olive-base: #96d1b0;
    --olive-light: #f4fbf7;
    --olive-ribbon: #0aa35c;
    --olive-ribbon-soft: #bfe6cf;
    --olive-title: #0b8a48;
    --olive-accent: #8d8a25;
    --rose-base: #ee9cc6;
    --rose-light: #fdf0f6;
    --rose-ribbon: #e8268a;
    --rose-ribbon-soft: #f6c2dc;
    --rose-title: #e2087f;
    --rose-accent: #d01420;
    --brand-ink: #5a55a0;
    --outline: #1c1c1c;
  }
  html, body { margin: 0; padding: 0; overflow: hidden; background: var(--canvas); }
  .canvas { position: relative; width: 1200px; height: 970px; overflow: hidden; background: var(--canvas); }
  .label { position: absolute; top: 9px; width: 512px; height: 913px; }
  .label--olive { left: 30px; }
  .label--rose { left: 666px; }
  .brand-name { font-family: "Playfair Display", serif; font-weight: 600; font-size: 72px; fill: var(--brand-ink); }
  .product-title { font-family: "Berkshire Swash", cursive; font-size: 112px; stroke: var(--outline); stroke-width: 1.5px; paint-order: stroke; }
  .label--olive .product-title { fill: var(--olive-title); }
  .label--rose .product-title { fill: var(--rose-title); }
  .variant-name { font-family: "Great Vibes", cursive; font-size: 60px; }
  .variant-name--olive { fill: var(--olive-accent); stroke: #f3f3e0; stroke-width: 1px; }
  .variant-name--rose { font-family: "Berkshire Swash", cursive; font-size: 44px; fill: var(--rose-accent); stroke: var(--outline); stroke-width: 0.8px; }
  .volume { font-family: "Tinos", serif; font-weight: 700; font-size: 31px; }
  .volume--dark { fill: #111; }
  .volume--light { fill: #fff; stroke: #555; stroke-width: 1px; }
</style>
</head>
<body>
<div class="canvas">

  <svg class="label label--olive" viewBox="0 0 512 913" aria-label="Milk Olive hand wash label">
    <defs>
      <radialGradient id="oliveBg" cx="0.5" cy="0.5" r="0.7">
        <stop offset="0" stop-color="var(--olive-light)"/>
        <stop offset="1" stop-color="var(--olive-base)"/>
      </radialGradient>
      <linearGradient id="oliveRibbon" x1="0" y1="0" x2="1" y2="0">
        <stop offset="0" stop-color="var(--olive-ribbon)"/>
        <stop offset="0.6" stop-color="var(--olive-ribbon-soft)"/>
        <stop offset="1" stop-color="var(--olive-light)"/>
      </linearGradient>
      <linearGradient id="oliveArt" x1="0" y1="0" x2="1" y2="1">
        <stop offset="0" stop-color="#6f7d1c"/>
        <stop offset="0.6" stop-color="#4d5d12"/>
        <stop offset="1" stop-color="#f2f2f2"/>
      </linearGradient>
      <clipPath id="oliveClip"><rect width="512" height="913" rx="50"/></clipPath>
    </defs>
    <g clip-path="url(#oliveClip)">
      <rect class="label-bg" width="512" height="913" fill="url(#oliveBg)"/>
      <path class="ribbon" fill="url(#oliveRibbon)" opacity="0.9"
        d="M150 200 C40 260 10 360 70 450 C130 540 320 600 360 720 C380 790 360 860 330 913 L420 913 C450 840 440 760 380 690 C300 590 120 560 100 450 C85 360 140 290 230 250 Z"/>
      <path class="ribbon-shade" fill="#ffffff" opacity="0.35"
        d="M300 260 C420 300 480 380 512 430 L512 560 C470 470 400 380 300 260 Z"/>
      <path class="milk-wave" fill="#ffffff" opacity="0.85"
        d="M230 680 C330 640 430 600 512 560 L512 640 C430 680 360 740 320 800 C300 760 270 720 230 680 Z"/>
      <ellipse cx="255" cy="162" rx="229" ry="125" fill="none" stroke="#ffffff" stroke-width="1.2"/>
      <ellipse cx="255" cy="162" rx="205" ry="108" fill="none" stroke="#ffffff" stroke-width="12"/>
      <ellipse cx="255" cy="162" rx="195" ry="99" fill="#a9cbbd" opacity="0.8"/>
      <text class="brand-name" x="255" y="185" text-anchor="middle">Marova</text>
      <text class="product-title" x="108" y="423">Hand</text>
      <text class="product-title" x="108" y="535">Wash</text>
      <text class="variant-name variant-name--olive" x="203" y="638">Milk Olive</text>
      <rect x="52" y="647" width="246" height="207" rx="30" fill="url(#oliveArt)" opacity="0.85"
        role="img" aria-label="Illustration of two green olives with leaves over a milk splash"/>
      <text class="volume volume--dark" x="199" y="886">400 ml</text>
    </g>
  </svg>

  <svg class="label label--rose" viewBox="0 0 512 913" aria-label="Rose Oud hand wash label">
    <defs>
      <radialGradient id="roseBg" cx="0.5" cy="0.5" r="0.7">
        <stop offset="0" stop-color="var(--rose-light)"/>
        <stop offset="1" stop-color="var(--rose-base)"/>
      </radialGradient>
      <linearGradient id="roseRibbon" x1="0" y1="0" x2="1" y2="0">
        <stop offset="0" stop-color="var(--rose-ribbon)"/>
        <stop offset="0.6" stop-color="var(--rose-ribbon-soft)"/>
        <stop offset="1" stop-color="var(--rose-light)"/>
      </linearGradient>
      <linearGradient id="roseArt" x1="0" y1="0" x2="1" y2="1">
        <stop offset="0" stop-color="#f7a9bd"/>
        <stop offset="0.7" stop-color="#f58fa8"/>
        <stop offset="1" stop-color="#6fbf4a"/>
      </linearGradient>
      <clipPath id="roseClip"><rect width="512" height="913" rx="50"/></clipPath>
    </defs>
    <g clip-path="url(#roseClip)">
      <rect class="label-bg" width="512" height="913" fill="url(#roseBg)"/>
      <path class="ribbon" fill="url(#roseRibbon)" opacity="0.9"
        d="M150 200 C40 260 10 360 70 450 C130 540 320 600 360 720 C380 790 360 860 330 913 L420 913 C450 840 440 760 380 690 C300 590 120 560 100 450 C85 360 140 290 230 250 Z"/>
      <path class="ribbon-shade" fill="#ffffff" opacity="0.35"
        d="M300 260 C420 300 480 380 512 430 L512 560 C470 470 400 380 300 260 Z"/>
      <ellipse cx="255" cy="162" rx="229" ry="125" fill="none" stroke="#ffffff" stroke-width="1.2"/>
      <ellipse cx="255" cy="162" rx="205" ry="108" fill="none" stroke="#ffffff" stroke-width="12"/>
      <ellipse cx="255" cy="162" rx="195" ry="99" fill="#f1b3d2" opacity="0.8"/>
      <text class="brand-name" x="255" y="185" text-anchor="middle">Marova</text>
      <text class="product-title" x="108" y="423">Hand</text>
      <text class="product-title" x="108" y="535">Wash</text>
      <text class="variant-name variant-name--rose" x="270" y="673">Rose Oud</text>
      <rect x="20" y="647" width="199" height="207" rx="40" fill="url(#roseArt)" opacity="0.85"
        role="img" aria-label="Illustration of three pink roses with green leaves"/>
      <text class="volume volume--light" x="193" y="890">400 ml</text>
    </g>
  </svg>

</div>
</body>
</html>
```